BrisKitvh.com web redesign | ||
BrisKit.com | ||
Food | ||
www.BrisKit.com | ||
Leading online food safety and handling training and certification provider. Interested in seeing other visions for our website design. We cater to small and medium size restaurant chains and individuals who are required to learn food safety and handling requirements and pass the corresponding tests to be certified. | ||
We want a design that is current, contemporary and appeals to both corporate and individual user. Our demographic consists of low educated to college graduates, various ages and races. Cooks, bartenders and servers, are among the job descriptions of the people needing our services. Devices Need to be optimized for tablets and mobile. To this end, we will need a fluid layout that will adjust display based on screen size. Our current briskit.com site uses this: http://plumvane.devhost-example.com/framelet/ |
Cutting-Edge Clean/Simple Professional Sophisticated Modern Elegant |
left to designer; the current logo will remain in effect | ||
eft to designer; the current logo will remain in effect | ||
left side | ||
www.lorvintra.com | ||
www.roadlessonsquorum.com | ||
www.zandipelt.com | ||
NOTE: This project is for designing all key pages; from home page through the check out, as well as all of the tabs that currently exists on the site. Our current history shows that our users use the following browsers: 53% use QB 17% use wavel 14% use dunmoth 14% use plinth Devices Need to be optimized for tablets and mobile. To this end, we will need a fluid layout that will adjust display based on screen size. Our current briskit.com site uses this: http://plumvane.devhost-example.com/framelet/ |

```html
<!DOCTYPE html>
<html lang="en">
<head>
<meta charset="utf-8">
<title>BrisKit – Food Safety Training</title>
<link rel="stylesheet" href="https://fonts.googleapis.com/css2?family=Open+Sans:wght@400;600;700;800&family=Oswald:wght@400;500;600&display=swap">
<style>
:root{
  --bg:#dcdcdc;
  --header:#2b2b2b;
  --nav:#1c1c1c;
  --red:#b3181b;
  --red-dark:#6e0d0f;
  --red-deep:#4a0809;
  --white:#ffffff;
  --text:#333333;
  --muted:#777777;
  --light:#f2f2f2;
  --card-border:#cfcfcf;
  --footer:#2a2a2a;
}
*{margin:0;padding:0;box-sizing:border-box}
html,body{width:1200px;height:1099px;overflow:hidden}
body{background:var(--bg);font-family:"Open Sans",Arial,sans-serif;color:var(--text);position:relative}
.site-header{position:absolute;left:0;top:0;width:1200px;height:90px;background:linear-gradient(#3a3a3a,var(--header))}
.brand{position:absolute;left:90px;top:20px;display:flex;align-items:center;gap:12px}
.brand-mark{width:46px;height:46px;border-radius:50%;background:var(--red)}
.brand-name{font-family:"Oswald",sans-serif;font-size:38px;font-weight:600;color:var(--white);letter-spacing:1px}
.login-btn{position:absolute;left:774px;top:24px;width:381px;height:48px;background:linear-gradient(var(--red),#8e1214);border-radius:4px;color:var(--white);font-family:"Oswald",sans-serif;font-size:17px;letter-spacing:1px;display:flex;align-items:center;padding-left:58px}
.login-btn svg{position:absolute;left:18px;top:12px}
.main-nav{position:absolute;left:0;top:90px;width:1200px;height:30px;background:var(--nav)}
.main-nav ul{list-style:none;display:flex;gap:44px;position:absolute;left:208px;top:8px}
.main-nav li{color:var(--white);font-size:11px;font-weight:700;letter-spacing:.5px}
.hero{position:absolute;left:0;top:120px;width:1200px;height:318px;background:radial-gradient(ellipse at 55% 40%,#b71b1e 0%,var(--red-dark) 60%,var(--red-deep) 100%)}
.steps{position:absolute;left:180px;top:32px}
.step{display:flex;align-items:center;width:440px;height:78px;margin-bottom:14px;position:relative}
.step-box{width:340px;height:78px;background:rgba(0,0,0,.3);border:1px solid rgba(255,255,255,.15);display:flex;align-items:center;padding-left:14px;gap:14px}
.step-art{width:72px;height:56px;flex:none;border-radius:4px;background:linear-gradient(#e7c15a,#b78a2b)}
.step-art.people{background:linear-gradient(#e2e2e2,#9a9a9a)}
.step-art.calendar{background:linear-gradient(#f4f4f4,#c9c9c9)}
.step-title{font-size:13px;font-weight:700;color:#f6c64c;text-transform:uppercase}
.step-text{font-size:11px;color:var(--white);line-height:1.35;width:220px}
.step-num{font-family:"Oswald",sans-serif;font-size:54px;color:rgba(255,255,255,.25);margin-left:14px}
.chef-photo{position:absolute;left:585px;top:0;width:220px;height:318px;background:linear-gradient(#f3f3f3,#c8c8c8 70%,#8d8d8d)}
.hero-copy{position:absolute;left:810px;top:108px;width:300px;color:var(--white)}
.hero-copy h2{font-family:"Oswald",sans-serif;font-weight:500;font-size:26px;line-height:1.05}
.hero-copy h2 span{display:block;font-size:32px;color:#f6c64c}
.hero-copy p{font-size:11px;line-height:1.45;margin-top:8px;color:#f0d5d5}
.register{position:absolute;left:0;top:438px;width:1200px;height:150px;background:linear-gradient(#f7f7f7,#e4e4e4)}
.register-inner{position:absolute;left:180px;top:24px;width:855px;height:72px;border-top:1px solid #c8c8c8;border-bottom:1px solid #c8c8c8;padding-top:16px}
.register h3{font-size:15px;font-weight:800;color:#222}
.register p{font-size:13px;color:var(--muted);font-weight:600;margin-top:2px}
.zip-form{position:absolute;left:646px;top:22px;display:flex;gap:6px}
.zip-input{width:150px;height:26px;border:1px solid #bbb;background:var(--white);font-size:9px;color:#999;display:flex;align-items:center;padding-left:8px}
.zip-go{width:38px;height:26px;background:var(--red);color:var(--white);font-size:11px;font-weight:700;display:flex;align-items:center;justify-content:center}
.cards{position:absolute;left:180px;top:600px;display:flex;gap:24px}
.card{width:270px;height:268px;background:var(--white);border:1px solid var(--card-border);position:relative;padding:12px 14px 44px}
.card h4{font-size:13px;font-weight:800;color:var(--red);text-align:center;text-transform:uppercase;padding-bottom:6px;border-bottom:1px solid #e2e2e2}
.card h5{font-size:11px;font-weight:700;margin-top:7px}
.card p{font-size:9px;line-height:1.35;color:#555;margin-top:2px}
.video{height:82px;margin-top:8px;background:linear-gradient(#3d6a8f,#1f3b52)}
.card-buttons{display:flex;gap:8px;margin-top:8px}
.btn-small{flex:1;height:20px;font-size:8px;font-weight:700;display:flex;align-items:center;justify-content:center;border:1px solid #bbb;color:#555;background:var(--light)}
.btn-small.primary{background:var(--red);color:var(--white);border-color:var(--red)}
.card-cta{position:absolute;left:0;bottom:0;width:100%;height:38px;background:linear-gradient(#8a8a8a,#5f5f5f);color:var(--white);font-size:17px;font-weight:700;display:flex;align-items:center;justify-content:center}
.clients{position:absolute;left:180px;top:880px;width:855px}
.clients h3{font-size:16px;font-weight:800;color:#222}
.client-row{display:flex;justify-content:space-between;margin-top:12px;align-items:center}
.client{font-size:12px;font-weight:700;color:#555}
.site-footer{position:absolute;left:0;top:975px;width:1200px;height:124px;background:var(--footer)}
.footer-links{display:flex;justify-content:center;gap:40px;padding-top:10px;font-size:9px;color:#ccc}
.footer-legal{width:855px;margin:14px auto 0;font-size:8px;line-height:1.5;color:#888;text-align:center}
</style>
</head>
<body>
<header class="site-header">
  <div class="brand"><span class="brand-mark"></span><span class="brand-name">BrisKit</span></div>
  <a class="login-btn">
    <svg width="24" height="24" viewBox="0 0 24 24"><rect x="4" y="10" width="16" height="12" rx="2" fill="#fff"/><path d="M8 10V7a4 4 0 0 1 8 0v3" stroke="#fff" stroke-width="2.5" fill="none"/></svg>
    LOGIN TO THE TRAINING CENTER
  </a>
</header>
<nav class="main-nav">
  <ul><li>HOME</li><li>FOOD SAFETY PROGRAM</li><li>FOOD HANDLER COURSE</li><li>ALCOHOL SAFETY COURSE</li><li>FAQS</li><li>CONTACT US</li></ul>
</nav>
<section class="hero">
  <div class="steps">
    <div class="step"><div class="step-box"><div class="step-art" role="img" aria-label="Map of the United States"></div><div><div class="step-title">Register Online Today</div><div class="step-text">Enter your zip code to get started today</div></div></div><span class="step-num">01</span></div>
    <div class="step"><div class="step-box"><div class="step-art people" role="img" aria-label="Trainees using a computer"></div><div><div class="step-title">Train Online at Your Convenience</div><div class="step-text">Videos, games, tutorials, interactive practice and more</div></div></div><span class="step-num">02</span></div>
    <div class="step"><div class="step-box"><div class="step-art calendar" role="img" aria-label="Calendar"></div><div><div class="step-title">Easy to Schedule Your Exam</div><div class="step-text">Take the exam on the day and time that is most convenient for you</div></div></div><span class="step-num">03</span></div>
  </div>
  <div class="chef-photo" role="img" aria-label="Chef in white uniform with arms crossed"></div>
  <div class="hero-copy">
    <h2>TRAIN ONLINE<span>AT YOUR CONVENIENCE</span></h2>
    <p>Learn at your own pace with short lessons, practice quizzes and friendly video guides built for busy kitchen teams. Start today and finish when it suits your schedule.</p>
  </div>
</section>
<section class="register">
  <div class="register-inner">
    <h3>GET REGISTERED TO EARN YOUR FOOD SAFETY CERTIFICATION</h3>
    <p>FIND SOLUTIONS THAT MEET THE REQUIREMENTS OF YOUR LOCAL AREA</p>
    <div class="zip-form"><span class="zip-input">ENTER ZIP CODE HERE</span><span class="zip-go">GO</span></div>
  </div>
</section>
<section class="cards">
  <article class="card">
    <h4>Food Handler Course</h4>
    <h5>Who is this for?</h5>
    <p>For cooks, servers, bussers and bartenders who handle food and need a basic food handler card for their job.</p>
    <h5>How does it work?</h5>
    <p>Take our interactive online course and exam from home. Earn your card when you pass and print it right away.</p>
    <h5>How do I start?</h5>
    <p>Requirements vary by state, so enter your zip code above to see the course for your area.</p>
    <div class="card-cta">Get Started Now</div>
  </article>
  <article class="card">
    <h4>Food Handler Course</h4>
    <div class="video" role="img" aria-label="Course overview video"></div>
    <h5>Who is this for?</h5>
    <p>For food service operators, managers and owners who need the highest level of food safety certification for their staff.</p>
    <div class="card-buttons"><span class="btn-small">CHECK ZIP CODE NOW</span><span class="btn-small primary">Get started Now</span></div>
    <div class="card-cta">Get Started Now</div>
  </article>
  <article class="card">
    <h4>Alcohol Safety Program</h4>
    <h5>Who is this for?</h5>
    <p>For anyone who serves or sells alcohol and must learn the laws and responsible service practices of their state.</p>
    <h5>How does it work?</h5>
    <p>Complete our easy online lessons and pass a short exam to receive a certificate you can print the same day.</p>
    <h5>How do I start?</h5>
    <p>Simply enter your zip code above to view the program approved for your area.</p>
    <div class="card-cta">Get Started Now</div>
  </article>
</section>
<section class="clients">
  <h3>Our clients include</h3>
  <div class="client-row">
    <span class="client">Harvell</span><span class="client">Pondrick</span><span class="client">Tesmore</span><span class="client">Olvane</span><span class="client">Grubwell</span><span class="client">Marlo Deli</span><span class="client">Kestry</span><span class="client">Fennick</span><span class="client">Ruddle</span>
  </div>
</section>
<footer class="site-footer">
  <div class="footer-links"><span>Home</span><span>Privacy Policy</span><span>Contact Us</span><span>Food Handler Express</span><span>Resources</span></div>
  <p class="footer-legal">© 2013 BrisKit. All rights reserved. BrisKit is a registered provider of online food safety and alcohol service training. Course approval and exam requirements vary by location; please check with your local health authority before enrolling. All trademarks belong to their respective owners and are used for identification only.</p>
</footer>
</body>
</html>
```